Letterhead Design for Law Firm

**Edit: I have added the photo of a bottom that I like.

------
We are looking for a re-design of our new letterhead. The letterhead is for a law firm and will be used for digital and traditionally printed correspondence.

Here are some suggestions:

- Please use colours are #8ec900 and simple black.
- Please do not use any type of "waves" at the bottom of the page. This is not in style at all.
- Please stay modern yet conservative.
- Please use font Segoe UI Light or similar if you can
- Avoid clipart or illustrations.
- Utilize ample white space in the layout so the design looks clean and information is easy to read at a glance. Don't overcrowd the letterhead.
- Make sure the letterhead design is consistent with our brand identity (see brambleford.ca)
-Please, no black headers or footers.

I am attaching my current letterhead and signature for your convenience.

Remember, the letterhead is an extension of our professional identity. We are a successful firm and trial lawyers who correspond with insurers, judges, lawyers, courts, clients, etc. Make it new, modern, attractive, yet powerful and conservative.

It needs to be easily printable. I would like the bleed removed in print so the black bar the bottom crosses the page (but the text is not near the edges)

Target Market(s)

Clients, Government Offices, Judiciary, Lawyers, Insurance Companies, Colleagues.

Industry/Entity Type

Law

Font styles to use
Other font styles liked:
• Segoe UI LIght, Calibri Light,

Colors
00AB8E
00BBA5
67D7C9
C6EFE9
E9F9F6

Requirements
Must have
• Everything that is on the letterhead now.
Nice to have
• Cutting Edge design, yet conservative.
Should not have
• law firm cliche design, images,

```html
<!DOCTYPE html>
<html lang="en">
<head>
<meta charset="utf-8">
<title>Marlowe Letterhead</title>
<link rel="stylesheet" href="https://fonts.googleapis.com/css2?family=Open+Sans:wght@300;400;600;700&display=swap">
<style>
  :root {
    --brand-green: #8ec900;
    --rule-green: #8dc63f;
    --ink: #000000;
    --text: #1a1a1a;
    --paper: #ffffff;
  }
  * { margin: 0; padding: 0; box-sizing: border-box; }
  html, body { width: 849px; height: 1200px; overflow: hidden; background: var(--paper); }
  .letterhead {
    position: relative;
    width: 849px;
    height: 1200px;
    overflow: hidden;
    font-family: "Open Sans", "Segoe UI", sans-serif;
    color: var(--text);
    background: var(--paper);
  }
  /* Brand block */
  .brand {
    position: absolute;
    left: 208px;
    top: 37px;
    width: 303px;
    text-align: center;
  }
  .brand__rule { height: 2px; background: var(--rule-green); }
  .brand__name {
    font-weight: 400;
    font-size: 56px;
    line-height: 72px;
    letter-spacing: 2px;
    padding-left: 2px;
    color: var(--ink);
    white-space: nowrap;
  }
  .brand__tagline {
    margin-top: 5px;
    font-weight: 400;
    font-size: 16px;
    letter-spacing: 1.6px;
    color: var(--text);
    white-space: nowrap;
  }
  /* Practice panel */
  .practice {
    position: absolute;
    left: 526px;
    top: 0;
    width: 186px;
    height: 145px;
    background: var(--brand-green);
    border-bottom-right-radius: 35px;
    padding: 38px 0 0 13px;
    font-size: 12.3px;
    line-height: 16.5px;
    font-weight: 300;
    color: var(--text);
    white-space: nowrap;
  }
  .practice__title { font-weight: 700; }
  /* Side bar */
  .sidebar-accent {
    position: absolute;
    left: 0;
    top: 205px;
    width: 35px;
    height: 80px;
    background: var(--brand-green);
    border-top-left-radius: 35px;
  }
  .sidebar {
    position: absolute;
    left: 0;
    top: 251px;
    width: 35px;
    bottom: 0;
    background: var(--ink);
    border-top-left-radius: 35px;
  }
  /* Footer */
  .footer-rule {
    position: absolute;
    height: 1.5px;
    background: var(--rule-green);
  }
  .footer-rule--top { left: 109px; top: 1108px; width: 626px; }
  .footer-rule--bottom { left: 107px; top: 1179px; width: 626px; }
  .contact-row {
    position: absolute;
    left: 109px;
    width: 626px;
    display: flex;
    align-items: center;
  }
  .contact-row--primary { top: 1114px; height: 26px; justify-content: space-between; padding: 0 14px 0 52px; }
  .contact-row--secondary { top: 1146px; height: 24px; justify-content: center; gap: 34px; }
  .contact {
    display: flex;
    align-items: center;
    font-size: 12.8px;
    font-weight: 300;
    white-space: nowrap;
    color: var(--text);
  }
  .contact svg { fill: var(--brand-green); flex: none; }
  .contact strong { font-weight: 600; }
</style>
</head>
<body>
<div class="letterhead">

  <header class="brand">
    <div class="brand__rule"></div>
    <div class="brand__name">MARLOWE</div>
    <div class="brand__rule"></div>
    <div class="brand__tagline">PERSONAL INJURY LAWYERS</div>
  </header>

  <aside class="practice">
    <div class="practice__title">Practice Restricted:</div>
    <div>Serious Personal Injury</div>
    <div>Wrongful Death Litigation</div>
    <div>Long-Term Disability Litigation</div>
    <div>Wrongful Dismissal Litigation</div>
    <div>Employee Terminations</div>
  </aside>

  <div class="sidebar-accent"></div>
  <div class="sidebar"></div>

  <footer>
    <div class="footer-rule footer-rule--top"></div>

    <div class="contact-row contact-row--primary">
      <div class="contact">
        <svg width="23" height="16" viewBox="0 0 23 16"><path d="M0 0h23v16H0z"/><path d="M1 1l10.5 8L22 1M1 15l7.5-7M22 15l-7.5-7" stroke="#fff" stroke-width="1.4" fill="none"/></svg>
        <span style="margin-left:10px;">clara@brambleford.ca</span>
      </div>
      <div class="contact">
        <svg width="18" height="26" viewBox="0 0 18 26"><path d="M3 1l4 0 1 7-3 2c1 4 3 8 6 10l3-2 4 4-2 4c-8-1-14-12-13-25z"/></svg>
        <span style="margin-left:8px;">905-555-0142</span>
      </div>
      <div class="contact">
        <svg width="24" height="20" viewBox="0 0 24 20"><path d="M5 0h12v7H5z M0 9h3v8h18V9h3v11H0z M6 9h12v6H6z"/><path d="M7 2.5h8M7 4.5h8" stroke="#fff" stroke-width="1"/></svg>
        <span style="margin-left:9px;">905-555-0178</span>
      </div>
      <div class="contact">
        <svg width="21" height="21" viewBox="0 0 21 21"><circle cx="10.5" cy="10.5" r="10.5"/><g stroke="#fff" stroke-width="1.1" fill="none"><ellipse cx="10.5" cy="10.5" rx="4.5" ry="10"/><path d="M10.5 0v21M0 10.5h21M2 5.5h17M2 15.5h17"/></g></svg>
        <span style="margin-left:9px;">www.brambleford.ca</span>
      </div>
    </div>

    <div class="contact-row contact-row--secondary">
      <div class="contact">
        <svg width="15" height="20" viewBox="0 0 15 20"><path d="M7.5 0a7.5 7.5 0 0 1 7.5 7.5c0 5-7.5 12.5-7.5 12.5S0 12.5 0 7.5A7.5 7.5 0 0 1 7.5 0z"/><circle cx="7.5" cy="7.5" r="3" fill="#fff"/></svg>
        <span style="margin-left:12px;">2 Elm Street W., Suite 1210 Hamilton, ON&nbsp;&nbsp;L8P 2B6</span>
      </div>
      <div class="contact">
        <svg width="18" height="23" viewBox="0 0 18 23"><circle cx="9" cy="6" r="6"/><path d="M0 23v-4c0-3 3-6 5-6l4 4 4-4c2 0 5 3 5 6v4z"/></svg>
        <span style="margin-left:8px;"><strong>File Clerk:</strong> Clara Whitfield</span>
      </div>
    </div>

    <div class="footer-rule footer-rule--bottom"></div>
  </footer>

</div>
</body>
</html>
```